I need a compelling, relevant cover for a book being published in January - title is the name of this project. The book is a call to action to women to become entrepreneurs as today's best path to achieving parity, purpose, prosperity and passion. See extended description of the book's message online at:
walkingtallneverrequireswalkingalone.example
(and attached pdf -- the cover art posted here is simply a placeholder/clip art ). I'm looking for something more emotional and exciting and distinctive and appropriate to the subject matter and message..
type on cover must include:
Standing Tall Won't Require Standing Alone
By Marcia T. Vellby
How Trusting Your Own Instincts Can Shift Your Path and Build Your Venture
With a Foreword by CEO Dorinda P. Halvorsen

Target Market(s)

Professional women, women business owners, aspiring women students, marketers who target women in business, such as IT providers; lenders and funders; financial services like credit card issuers -- anyone who sells to women i biz. Women's networking groups,entrepreneurship divisions at universities, and associations. International audience but tilted toward US readers.

Industry/Entity Type

Call

Font styles to use
Serif

Requirements
Nice to have
• Something that stands out from the crowd -- that would make a woman want to pick up the book because it "speaks" her language/values. Something that addresses contemporary, up-to-date ideas about gender equity/sex roles/women's advancement
Should not have
• NOTHING PINK! Please avoid "empowerment" looks and ideas (too cliche) and avoid traditional business images, like briefcases

```html
<!DOCTYPE html>
<html lang="en">
<head>
<meta charset="utf-8">
<title>Standing Tall Won't Require Standing Alone — Book Cover</title>
<link href="https://fonts.googleapis.com/css2?family=Bodoni+Moda:opsz,wght@6..96,400;6..96,700&display=swap" rel="stylesheet">
<style>
  :root {
    --cover-yellow: #fbe62c;
    --title-red: #e8432f;
    --accent-white: #ffffff;
    --ink-black: #1a1a1a;
  }
  html, body {
    margin: 0;
    padding: 0;
    width: 781px;
    height: 1200px;
    overflow: hidden;
    background: var(--cover-yellow);
  }
  .book-cover {
    position: relative;
    width: 781px;
    height: 1200px;
    background: var(--cover-yellow);
    font-family: "Bodoni Moda", "Didot", serif;
  }
  .rule-marks {
    position: absolute;
    left: 0;
    top: 0;
  }
  .book-title {
    position: absolute;
    left: 125px;
    top: 262px;
    margin: 0;
    font-weight: 700;
    font-size: 60px;
    line-height: 66px;
    color: var(--title-red);
    letter-spacing: -0.5px;
  }
  .book-title .title-line { display: block; white-space: nowrap; }
  .book-title .title-accent { color: var(--accent-white); }
  .book-subtitle {
    position: absolute;
    left: 125px;
    top: 682px;
    margin: 0;
    font-size: 17px;
    font-weight: 700;
    color: var(--ink-black);
    line-height: 74px;
  }
  .subtitle-line { display: block; white-space: nowrap; }
  .highlight {
    background: linear-gradient(to bottom, transparent 55%, var(--accent-white) 55%, var(--accent-white) 100%);
    padding: 0 2px 2px 0;
  }
  .foreword-credit { font-weight: 400; }
  .book-author {
    position: absolute;
    left: 372px;
    top: 1088px;
    margin: 0;
    font-size: 32px;
    font-weight: 700;
    color: var(--title-red);
    white-space: nowrap;
  }
</style>
</head>
<body>
  <main class="book-cover">
    <svg class="rule-marks" width="781" height="260" viewBox="0 0 781 260" aria-hidden="true">
      <rect x="36" y="45" width="136" height="5" fill="var(--title-red)"/>
      <rect x="36" y="92" width="136" height="5" fill="var(--title-red)"/>
      <rect x="520" y="206" width="58" height="3" fill="var(--ink-black)"/>
      <rect x="520" y="224" width="58" height="3" fill="var(--ink-black)"/>
    </svg>

    <h1 class="book-title">
      <span class="title-line">Standing <span class="title-accent">Tall</span> Won't</span>
      <span class="title-line">Require Standing</span>
      <span class="title-line">Alone</span>
    </h1>

    <p class="book-subtitle">
      <span class="subtitle-line"><span class="highlight">How trusting your own instincts can shift</span></span>
      <span class="subtitle-line"><span class="highlight">your path and build your venture.</span> <span class="foreword-credit">CEO, Dorinda P. Halvorsen</span></span>
    </p>

    <p class="book-author">By Marcia T. Vellby</p>
  </main>
</body>
</html>
```